New Brochure Design Project - downloadable PDF

Capability Statement, Brochure and Website - we are looking for a uniform of the three marketing assets that deliver a professional look and feel for executive-level decision-makers. Our company provides guest and patient-facing technologies. For the most part, the technologies are: smart TVs, Wi-Fi, RTLS, Integrated services. I have submitted the editable files we have, but in terms of industry images, we are happy to have others recommended. I have also submitted previous efforts and one Capability Statement from a company (KMB) that is well received.
Updates
Need extra days to review
Target Market(s)
Corporate and Government Procurement (Healthtcare and Hotels/Resorts)
Industry/Entity Type
Healthcare and Hotel/Resorts
Look and feel

```html
<!DOCTYPE html>
<html lang="en">
<head>
<meta charset="utf-8">
<title>Northvale Capability Statement Covers</title>
<link rel="stylesheet" href="https://fonts.googleapis.com/css2?family=Arimo:wght@400;700&family=Roboto+Condensed:wght@400&display=swap">
<style>
  :root {
    --backdrop: #d2d2d2;
    --paper: #ffffff;
    --brand-red: #d9060c;
    --slate: #4d6264;
    --ink-light: #ffffff;
    --photo-cream: #efeadc;
    --photo-blue: #8fb4e0;
    --photo-warm: #e7ddd0;
    --photo-skin: #d9b79c;
  }
  * { margin: 0; padding: 0; box-sizing: border-box; }
  html, body { width: 1200px; height: 900px; overflow: hidden; }
  body {
    background: var(--backdrop);
    font-family: "Arimo", Arial, sans-serif;
    display: flex;
    justify-content: center;
    align-items: center;
    gap: 24px;
  }
  .cover {
    position: relative;
    width: 400px;
    height: 566px;
    background: var(--paper);
    padding: 16px;
    box-shadow: 0 6px 18px rgba(0,0,0,0.18);
  }
  .cover-inner {
    position: relative;
    width: 100%;
    height: 100%;
    overflow: hidden;
  }
  .photo { position: absolute; inset: 0; }
  .photo--back {
    background: linear-gradient(115deg, var(--photo-cream) 0%, var(--photo-cream) 45%, var(--photo-blue) 75%, #5f7fb0 100%);
  }
  .photo--front {
    background: linear-gradient(125deg, #c9c6c0 0%, var(--photo-warm) 35%, var(--photo-skin) 65%, #f0ece6 100%);
  }
  .band { position: absolute; left: 0; bottom: 0; width: 100%; height: 200px; }
  .band-content {
    position: absolute;
    left: 0; right: 0; bottom: 0;
    color: var(--ink-light);
    padding: 0 22px 22px;
  }
  .brand-name {
    display: flex;
    align-items: center;
    gap: 8px;
    font-weight: 700;
    font-size: 19px;
    letter-spacing: 0.2px;
  }
  .brand-name .brand-dot {
    width: 10px; height: 10px;
    background: var(--ink-light);
  }
  .back-band-content {
    display: flex;
    justify-content: space-between;
    align-items: flex-end;
  }
  .tagline {
    margin-top: 10px;
    font-size: 12px;
    line-height: 1.35;
    max-width: 170px;
  }
  .contact {
    font-size: 7px;
    line-height: 1.5;
    text-align: left;
    margin-bottom: 48px;
  }
  .contact p + p { margin-top: 6px; }
  .doc-title {
    margin-top: 14px;
    font-family: "Roboto Condensed", "Arial Narrow", sans-serif;
    font-size: 27px;
    font-weight: 400;
  }
</style>
</head>
<body>

  <section class="cover cover--back">
    <div class="cover-inner">
      <div class="photo photo--back" role="img" aria-label="Photo of a smiling woman in a blue shirt pointing a TV remote"></div>
      <svg class="band" viewBox="0 0 368 200" preserveAspectRatio="none" aria-hidden="true">
        <path d="M0 70 Q190 40 368 0 L368 200 L0 200 Z" fill="var(--brand-red)"/>
      </svg>
      <div class="band-content back-band-content">
        <div class="back-identity">
          <div class="brand-name"><span class="brand-dot"></span>Northvale</div>
          <p class="tagline">The innovative solution for Hospitality, Television, Movie and Wi-Fi Services</p>
        </div>
        <div class="contact">
          <p>14 Harbour Lane, Eastfield QLD 4000<br>northvale-media.com</p>
          <p>Sam Keller, CEO · 0400 000 123<br>sam@northvale-media.com</p>
        </div>
      </div>
    </div>
  </section>

  <section class="cover cover--front">
    <div class="cover-inner">
      <div class="photo photo--front" role="img" aria-label="Photo of a smiling couple on a sofa holding a TV remote"></div>
      <svg class="band" viewBox="0 0 368 200" preserveAspectRatio="none" aria-hidden="true">
        <path d="M0 50 Q200 30 368 0 L368 200 L0 200 Z" fill="var(--slate)"/>
      </svg>
      <div class="band-content">
        <div class="brand-name"><span class="brand-dot"></span>Northvale</div>
        <h1 class="doc-title">Capability Statement</h1>
      </div>
    </div>
  </section>

</body>
</html>
```